Bright Sprout Sessions Brochure Project

Design a brochure that outlines the mindfulness programs I deliver and pricing. I will use this brochure to give to schools to promote my programs. Will have info about mindfulness and benefits, outline for each program I offer as well as prices and contact details. Contact details can be found at www.calmbrookhaven.com.au

Target Market(s)

Schools and community groups

Industry/Entity Type

Wellbeing and health

Font styles to use
Serif
Other font styles liked:
• open to suggestions

Colors
0094D4
00A9DD
6FCCEA
C7EBF8
E9F6FB

Requirements
Must have
• Title page, content as provided, my contact details and socials. Images and professional

```html
<!DOCTYPE html>
<html lang="en">
<head>
<meta charset="utf-8">
<title>Bright Sprout Sessions Brochure</title>
<link href="https://fonts.googleapis.com/css2?family=Lora:wght@400;600;700&family=Open+Sans:wght@400;600;700&display=swap" rel="stylesheet">
<style>
  :root{
    --blue-deep:#0094D4;
    --blue:#00A9DD;
    --blue-soft:#6FCCEA;
    --blue-pale:#C7EBF8;
    --blue-mist:#E9F6FB;
    --orange:#F39A1E;
    --yellow:#F6C623;
    --ink:#3d4650;
    --white:#ffffff;
    --photo-green:#8fb86a;
    --photo-warm:#d9b48f;
  }
  *{box-sizing:border-box;margin:0;padding:0}
  html,body{width:829px;height:1200px;overflow:hidden;background:var(--white)}
  body{position:relative;font-family:"Open Sans",Arial,sans-serif;color:var(--ink)}
  .spread{position:absolute;left:34px;width:760px;height:270px;display:flex;box-shadow:0 2px 6px rgba(0,0,0,.18)}
  .page{position:relative;width:380px;height:270px;overflow:hidden;background:var(--white)}
  .page + .page{border-left:1px solid #e3e8ec}
  .photo{position:absolute}
  .heading{position:absolute;font-family:"Lora",Georgia,serif;font-weight:700;color:var(--blue-deep);line-height:1.2}
  .subheading{font-family:"Lora",Georgia,serif;font-weight:700;color:var(--blue-deep);font-size:5.6px;margin:3px 0 2px}
  .body-text{position:absolute;font-size:4.3px;line-height:6px;color:var(--ink)}
  .body-text p{margin-bottom:3px}
  .body-text ul{list-style:none;margin-bottom:3px}
  .body-text li{padding-left:6px;position:relative}
  .body-text li::before{content:"";position:absolute;left:0;top:2px;width:3px;height:3px;border-radius:50%;background:var(--blue)}
  .body-text.light{color:var(--white)}
  .brand{font-family:"Lora",Georgia,serif;font-weight:700;color:var(--blue-deep)}
  .dot{display:inline-block;width:8px;height:8px;border-radius:50%;background:var(--blue-soft);vertical-align:middle;margin-right:3px}
  .band{position:absolute;left:0;width:100%}
  .table{position:absolute;border-collapse:collapse;font-size:4.2px;line-height:5px}
  .table th{background:var(--blue-deep);color:var(--white);text-align:left;padding:1.5px 3px;font-weight:700}
  .table td{padding:1.5px 3px;border-bottom:1px solid var(--blue-pale)}
  .table tr:nth-child(even) td{background:var(--blue-mist)}
  .badge{position:absolute;border-radius:50%;background:var(--blue-soft);border:3px solid var(--white)}
  .pill{position:absolute;background:var(--orange);color:var(--white);font-size:4.4px;font-weight:600;padding:3px 8px;border-radius:2px}
  .bubble{position:absolute;border-radius:50%}
  .socials{display:flex;justify-content:center;gap:10px;font-size:4.6px;margin-top:5px}
  .socials span::before{content:"";display:inline-block;width:5px;height:5px;border-radius:50%;background:var(--blue);margin-right:2px;vertical-align:-1px}
  .icon{width:5px;height:5px;vertical-align:-1px;margin-right:2px}
</style>
</head>
<body>

<!-- Spread 1: back cover + front cover -->
<section class="spread" style="top:27px">
  <div class="page back-cover">
    <div class="band" style="top:0;height:175px;background:linear-gradient(180deg,var(--blue) 0%,var(--blue-soft) 100%)"></div>
    <svg class="band" style="top:145px" width="380" height="60" viewBox="0 0 380 60"><path d="M0 30 Q190 -10 380 30 L380 60 L0 60Z" fill="#fff"/></svg>
    <div class="brand" style="position:absolute;top:16px;width:100%;text-align:center;color:var(--white);font-size:11px">Calmbrook Haven</div>
    <div class="body-text light" style="top:38px;left:26px;width:150px;font-size:4.1px">
      <p>Calmbrook Haven helps children build calm minds, kind hearts and strong resilience through simple, playful mindfulness practice.</p>
      <p>Sessions combine breathing, movement, stories and reflection, giving young people practical tools they can use in class, in the playground and at home.</p>
      <p>Every program is grounded in positive psychology and tailored to the age and needs of each group.</p>
    </div>
    <div class="body-text light" style="top:38px;left:198px;width:156px;font-size:4.1px">
      <p>Programs run for individual children, whole classes, small groups and community organisations across the region.</p>
      <p>Teachers and parents receive take-home resources so practice continues between sessions and becomes a daily habit.</p>
      <p>Get in touch to discuss a program that suits your school or group.</p>
    </div>
    <div style="position:absolute;top:192px;width:100%;text-align:center">
      <div class="brand" style="font-size:8.5px">Bright Sprout Sessions</div>
      <div style="font-size:4.6px;margin-top:5px">
        <svg class="icon" viewBox="0 0 10 10"><path d="M2 1h2l1 2-1 1a5 5 0 0 0 2 2l1-1 2 1v2a1 1 0 0 1-1 1A8 8 0 0 1 1 2a1 1 0 0 1 1-1z" fill="var(--blue-deep)"/></svg>0400 123 456 &nbsp;·&nbsp; hello@calmbrookhaven.com.au</div>
      <div style="font-size:4.6px;margin-top:3px;color:var(--blue-deep)">www.calmbrookhaven.com.au</div>
      <div class="socials"><span>/calmbrookhaven</span><span>@calmbrookhaven</span></div>
    </div>
  </div>
  <div class="page front-cover">
    <div class="photo" role="img" aria-label="Photo of smiling children lying in a circle on grass" style="left:0;top:0;width:380px;height:185px;background:linear-gradient(160deg,var(--photo-green),#c9d98f 60%,var(--photo-warm))"></div>
    <svg class="band" style="top:150px" width="380" height="120" viewBox="0 0 380 120"><path d="M0 60 Q120 0 380 30 L380 120 L0 120Z" fill="var(--blue-soft)"/><path d="M0 72 Q130 14 380 42 L380 120 L0 120Z" fill="#fff"/></svg>
    <div style="position:absolute;left:26px;top:206px"><span class="dot"></span><span class="brand" style="font-size:8.5px">Calmbrook Haven</span></div>
    <div style="position:absolute;left:26px;top:224px;font-family:'Lora',Georgia,serif;font-weight:700;font-size:9px;color:var(--white);background:var(--blue);padding:3px 8px;border-radius:2px">Bright Sprout Sessions</div>
    <div class="heading" style="right:20px;top:198px;width:160px;text-align:right;font-size:5.8px;line-height:8px;font-weight:600">MINDFULNESS AND POSITIVE PSYCHOLOGY PROGRAMS FOR CHILDREN</div>
    <div style="position:absolute;right:20px;top:250px;font-size:4.6px;color:var(--blue-deep)">www.calmbrookhaven.com.au</div>
  </div>
</section>

<!-- Spread 2: Mental Health Matters + Introduction to Mindfulness -->
<section class="spread" style="top:319px">
  <div class="page">
    <div class="photo" role="img" aria-label="Photo strip of children playing outdoors" style="left:0;top:0;width:380px;height:78px;background:linear-gradient(90deg,var(--photo-green),var(--photo-warm))"></div>
    <div class="bubble" role="img" aria-label="Circular photo of children laughing" style="left:132px;top:42px;width:58px;height:58px;background:var(--photo-warm);border:3px solid var(--white)"></div>
    <div class="bubble" role="img" aria-label="Circular photo of a child playing" style="left:196px;top:50px;width:48px;height:48px;background:var(--photo-green);border:3px solid var(--white)"></div>
    <div class="bubble" style="left:110px;top:90px;width:12px;height:12px;background:var(--yellow)"></div>
    <div class="bubble" style="left:250px;top:92px;width:8px;height:8px;background:var(--orange)"></div>
    <div class="heading" style="left:0;width:100%;text-align:center;top:106px;font-size:9px">Mental Health Matters</div>
    <div class="body-text" style="left:24px;top:122px;width:332px">
      <p>Around one in seven young people will experience a mental health challenge in any year, and half of all lifelong conditions begin before the age of fourteen. Early support makes a real difference, giving children tools to cope with stress, worry and big emotions before they grow into bigger problems.</p>
      <p>Schools are ideally placed to help. Mindfulness and positive psychology teach attention, self-kindness and resilience in ways that fit easily into a busy school day, and they benefit every child, not only those who are struggling.</p>
      <p>Research shows regular practice can improve focus, memory, sleep and emotional balance. Children become better at noticing how they feel, calming their bodies and choosing how to respond, which leads to kinder friendships and more settled classrooms.</p>
      <p>Teachers also benefit. Calmer students mean fewer disruptions, more time for learning and a more positive culture across the whole school community.</p>
      <p>Our programs are practical, fun and age appropriate, helping children carry these skills with them as they grow into confident, caring and resilient young adults.</p>
    </div>
  </div>
  <div class="page">
    <div class="photo" role="img" aria-label="Photo of children sitting together in a classroom" style="left:0;top:0;width:150px;height:118px;background:linear-gradient(135deg,var(--photo-warm),var(--blue-pale))"></div>
    <div class="heading" style="left:162px;top:16px;font-size:8.5px">Introduction to Mindfulness</div>
    <div class="body-text" style="left:162px;top:32px;width:196px">
      <p>Mindfulness is paying attention to the present moment with curiosity and care. Rather than being caught up in worries about the past or future, children learn to notice what is happening right now.</p>
      <p>Through simple practices such as mindful breathing, listening, eating and movement, children learn to pause before reacting and to treat themselves and others with kindness.</p>
      <p>Positive psychology complements this by exploring strengths, gratitude, optimism and meaningful goals.</p>
      <div class="subheading">Benefits for children</div>
      <ul>
        <li>Better concentration and learning</li>
        <li>Calmer responses to stress and change</li>
        <li>Stronger self-awareness and confidence</li>
        <li>Kinder relationships with others</li>
        <li>Improved sleep and mood</li>
      </ul>
    </div>
    <div class="body-text" style="left:16px;top:126px;width:134px">
      <div class="subheading" style="margin-top:0">Why start young?</div>
      <p>The developing brain is highly adaptable. Skills practised in childhood become natural habits that support wellbeing for life.</p>
      <p>Short daily practice of just a few minutes is enough to make a lasting difference at school and at home.</p>
      <div class="subheading">Benefits for schools</div>
      <ul>
        <li>More settled classrooms</li>
        <li>Fewer behaviour incidents</li>
        <li>Support for staff wellbeing</li>
      </ul>
    </div>
    <svg class="band" style="bottom:0" width="380" height="30" viewBox="0 0 380 30"><path d="M0 20 Q190 0 380 16 L380 30 L0 30Z" fill="var(--blue-pale)"/></svg>
  </div>
</section>

<!-- Spread 3: Programs overview + School program -->
<section class="spread" style="top:611px">
  <div class="page">
    <div class="photo" role="img" aria-label="Photo of smiling children holding a welcome sign" style="left:0;top:0;width:140px;height:270px;background:linear-gradient(180deg,var(--blue-pale),var(--photo-warm))"></div>
    <div class="bubble" style="left:124px;top:200px;width:14px;height:14px;background:var(--yellow)"></div>
    <div class="heading" style="left:154px;top:18px;width:210px;font-size:8.5px;line-height:10.5px">Mindfulness Program for Individuals, Schools and Community Groups</div>
    <div class="body-text" style="left:154px;top:46px;width:206px">
      <p>Each program blends breathing, movement, stories, games and reflection to build calm, focused and caring young people. Activities are hands-on and designed to be enjoyable, so children look forward to every session.</p>
      <p>Sessions run weekly and can be delivered in classrooms, small groups or one-on-one. Content is adapted for early years, primary and lower secondary students.</p>
      <p>Topics include understanding the brain, mindful breathing, managing big feelings, gratitude, kindness, self-compassion, focus and positive relationships.</p>
      <p>Every child receives a practice booklet, and teachers and parents are given simple resources so learning continues between sessions.</p>
      <p>Programs are delivered by an experienced facilitator with a background in education and wellbeing, and can be shaped around your school's existing wellbeing goals.</p>
      <p>Community groups, sports clubs and holiday programs are also welcome to enquire about tailored sessions.</p>
    </div>
    <div class="pill" style="left:154px;top:236px">Book a session today</div>
  </div>
  <div class="page">
    <div class="photo" role="img" aria-label="Photo of a smiling boy" style="left:0;top:0;width:160px;height:270px;background:linear-gradient(135deg,var(--photo-warm),var(--blue-soft))"></div>
    <div class="badge" role="img" aria-label="Program badge" style="left:118px;top:150px;width:52px;height:52px"></div>
    <div class="heading" style="left:180px;top:16px;font-size:7.5px">School Program</div>
    <div class="body-text" style="left:180px;top:28px;width:180px"><p>Eight weekly sessions for whole classes, tailored to each year level. Each session runs for 45 minutes.</p></div>
    <table class="table" style="left:180px;top:44px;width:180px">
      <tr><th>Week</th><th>Focus</th></tr>
      <tr><td>1</td><td>What is mindfulness?</td></tr>
      <tr><td>2</td><td>Breathing and the body</td></tr>
      <tr><td>3</td><td>Understanding feelings</td></tr>
      <tr><td>4</td><td>Thoughts and worries</td></tr>
      <tr><td>5</td><td>Kindness and gratitude</td></tr>
      <tr><td>6–8</td><td>Strengths and review</td></tr>
    </table>
    <div class="heading" style="left:180px;top:112px;font-size:7.5px">Small Group Program</div>
    <div class="body-text" style="left:180px;top:124px;width:180px"><p>Six sessions for up to eight children needing extra support with anxiety, focus or friendships.</p></div>
    <table class="table" style="left:180px;top:140px;width:180px">
      <tr><th>Session</th><th>Details</th></tr>
      <tr><td>Length</td><td>45 minutes</td></tr>
      <tr><td>Group size</td><td>Up to 8 children</td></tr>
      <tr><td>Resources</td><td>Booklet included</td></tr>
    </table>
    <div class="heading" style="left:180px;top:188px;font-size:7.5px">Staff Session</div>
    <div class="body-text" style="left:180px;top:200px;width:180px"><p>A practical after-school workshop helping teachers use short mindful moments in class and care for their own wellbeing.</p></div>
  </div>
</section>

<!-- Spread 4: Individual program + pricing -->
<section class="spread" style="top:903px">
  <div class="page">
    <div class="photo" role="img" aria-label="Photo of a smiling young girl" style="left:0;top:0;width:140px;height:270px;background:linear-gradient(180deg,var(--photo-warm),var(--blue-pale))"></div>
    <div class="badge" role="img" aria-label="Program badge" style="left:100px;top:22px;width:56px;height:56px"></div>
    <div class="heading" style="left:172px;top:16px;font-size:7.5px">Individual Program</div>
    <div class="body-text" style="left:172px;top:28px;width:188px"><p>One-on-one sessions shaped around each child's needs and goals, held in a calm and welcoming space.</p></div>
    <table class="table" style="left:172px;top:44px;width:188px">
      <tr><th>Session</th><th>Focus</th></tr>
      <tr><td>1</td><td>Getting to know you</td></tr>
      <tr><td>2</td><td>Calm breathing tools</td></tr>
      <tr><td>3</td><td>Naming big feelings</td></tr>
      <tr><td>4</td><td>Managing worries</td></tr>
      <tr><td>5</td><td>Strengths and next steps</td></tr>
    </table>
    <div class="heading" style="left:172px;top:106px;font-size:7.5px">Parent Support</div>
    <div class="body-text" style="left:172px;top:118px;width:188px"><p>Parents learn the same skills their children practise, making it easy to support calm routines at home.</p></div>
    <table class="table" style="left:172px;top:134px;width:188px">
      <tr><th>Option</th><th>Details</th></tr>
      <tr><td>Workshop</td><td>90 minutes</td></tr>
      <tr><td>Home pack</td><td>Included</td></tr>
      <tr><td>Follow-up call</td><td>30 minutes</td></tr>
    </table>
    <div class="heading" style="left:172px;top:176px;font-size:7.5px">Community Groups</div>
    <div class="body-text" style="left:172px;top:188px;width:188px"><p>Flexible sessions for clubs, libraries and holiday programs. Length and content are tailored to your group, with all materials provided.</p><p>Contact us for a quote and available dates.</p></div>
  </div>
  <div class="page">
    <div class="photo" role="img" aria-label="Photo of a group of children smiling outdoors" style="left:0;top:0;width:380px;height:100px;background:linear-gradient(90deg,var(--photo-green),var(--photo-warm))"></div>
    <svg class="band" style="top:82px" width="380" height="30" viewBox="0 0 380 30"><path d="M0 20 Q190 0 380 15 L380 30 L0 30Z" fill="#fff"/></svg>
    <div class="heading" style="left:22px;top:112px;font-size:7.5px">Pricing – School Programs</div>
    <table class="table" style="left:22px;top:126px;width:160px">
      <tr><th>Program</th><th>Price</th></tr>
      <tr><td>Class, 8 weeks</td><td>$960</td></tr>
      <tr><td>Small group, 6 weeks</td><td>$480</td></tr>
      <tr><td>Staff session</td><td>$250</td></tr>
      <tr><td>Parent evening</td><td>$200</td></tr>
    </table>
    <div class="heading" style="left:198px;top:112px;font-size:7.5px">Pricing – One on One</div>
    <table class="table" style="left:198px;top:126px;width:160px">
      <tr><th>Program</th><th>Price</th></tr>
      <tr><td>Single session</td><td>$90</td></tr>
      <tr><td>5 sessions</td><td>$420</td></tr>
      <tr><td>Parent workshop</td><td>$60</td></tr>
      <tr><td>Follow-up call</td><td>$40</td></tr>
    </table>
    <div class="body-text" style="left:22px;top:182px;width:336px">
      <p>All prices include GST and resources. Discounts are available for multiple classes and for schools booking a full year of programs. Travel outside the local area may incur a small fee.</p>
      <p><strong style="color:var(--blue-deep)">Bookings:</strong> 0400 123 456 · hello@calmbrookhaven.com.au · www.calmbrookhaven.com.au</p>
      <p><strong style="color:var(--blue-deep)">Follow us:</strong> /calmbrookhaven · @calmbrookhaven</p>
    </div>
    <svg class="band" style="bottom:0" width="380" height="26" viewBox="0 0 380 26"><path d="M0 16 Q190 0 380 12 L380 26 L0 26Z" fill="var(--blue-pale)"/></svg>
  </div>
</section>

</body>
</html>
```